Harborview Wellness Counseling
7 business cards, letterhead, envlp, fax cover
Harborview Wellness Counseling -
Creative Brief
Professional
Martin Oakridge
Owner/Manager
2875 Pellham Ridge Blvd. Suite 204 Larkfield, KS 63412
oakridgehome@brisknet-mail.net
I need cards for each of my seven therapists. I will upload word file with their names and info. Letterhead should not use therapists names.

```html
<!DOCTYPE html>
<html lang="en">
<head>
<meta charset="utf-8">
<title>Harborview Wellness Counseling – Stationery</title>
<link rel="stylesheet" href="https://fonts.googleapis.com/css2?family=Libre+Baskerville:wght@400;700&family=Open+Sans:wght@400;600&display=swap">
<style>
  :root {
    --navy: #1d3563;
    --navy-mid: #4a6796;
    --paper: #ffffff;
    --stage: #ffffff;
    --frame: #d6d8dc;
    --ink: #2a3d66;
    --accent: #e48a2a;
    --faint: #d9e1ec;
    --flap-line: #9aa1ab;
    --shadow: rgba(0, 0, 0, 0.22);
  }
  * { box-sizing: border-box; margin: 0; padding: 0; }
  html, body { width: 1200px; height: 741px; overflow: hidden; background: var(--stage); }
  .canvas { position: relative; width: 1200px; height: 741px; background: var(--stage); }
  .canvas-frame { position: absolute; left: 12px; top: 10px; width: 1176px; height: 721px; border: 1px solid var(--frame); }

  .sheet { position: absolute; background: var(--paper); box-shadow: 2px 3px 6px var(--shadow); overflow: hidden; }

  .wordmark { display: flex; align-items: center; gap: 5px; font-family: "Libre Baskerville", serif; font-weight: 700; color: var(--navy); text-transform: uppercase; white-space: nowrap; }
  .wordmark-dot { border-radius: 50%; background: var(--accent); flex: none; }

  /* Envelope front */
  .envelope-front { left: 62px; top: 163px; width: 408px; height: 187px;
    background: linear-gradient(to bottom, var(--navy) 0%, var(--navy-mid) 9%, #c9d3e3 28%, var(--paper) 48%); }
  .envelope-front .wordmark { position: absolute; left: 14px; top: 15px; font-size: 8.5px; }
  .envelope-front .wordmark-dot { width: 11px; height: 11px; }
  .return-address { position: absolute; left: 34px; top: 35px; font-family: "Open Sans", sans-serif; font-size: 5.5px; line-height: 1.45; color: var(--ink); font-weight: 600; }

  /* Envelope back */
  .envelope-back { left: 62px; top: 398px; width: 408px; height: 202px; }
  .envelope-back svg { position: absolute; inset: 0; }
  .envelope-back .wordmark { position: absolute; left: 50%; top: 40px; transform: translateX(-50%); font-size: 6px; }
  .envelope-back .wordmark-dot { width: 10px; height: 10px; }

  /* Letterhead */
  .letterhead { left: 629px; top: 91px; width: 297px; height: 567px;
    background: linear-gradient(to bottom, var(--navy) 0%, var(--navy-mid) 3%, #c3cee0 9%, var(--paper) 16%); }
  .letterhead .wordmark { position: absolute; left: 32px; top: 31px; font-size: 8.5px; }
  .letterhead .wordmark-dot { width: 12px; height: 12px; }
  .letterhead-emblem { position: absolute; left: 96px; top: 170px; width: 106px; height: 106px; border-radius: 50%; background: var(--faint); opacity: 0.7; }
  .letterhead-footer { position: absolute; left: 0; right: 0; bottom: 30px; text-align: center; font-family: "Open Sans", sans-serif; font-size: 4.6px; color: var(--ink); font-weight: 600; }

  /* Business card */
  .business-card { left: 967px; top: 312px; width: 163px; height: 84px;
    background: linear-gradient(to bottom, var(--navy) 0%, var(--navy-mid) 18%, #b7c5db 40%, var(--paper) 62%); }
  .card-name { position: absolute; right: 10px; top: 9px; text-align: right; font-family: "Open Sans", sans-serif; color: #fff; }
  .card-name strong { display: block; font-size: 6px; font-weight: 600; }
  .card-name span { display: block; font-size: 4.4px; }
  .card-contact { position: absolute; left: 10px; top: 32px; font-family: "Open Sans", sans-serif; font-size: 3.8px; line-height: 1.55; color: var(--ink); }
  .business-card .wordmark { position: absolute; right: 8px; bottom: 8px; font-size: 5px; }
  .business-card .wordmark-dot { width: 7px; height: 7px; }
</style>
</head>
<body>
<main class="canvas">
  <div class="canvas-frame"></div>

  <section class="sheet envelope-front" aria-label="Envelope front">
    <div class="wordmark"><span class="wordmark-dot"></span>Harborview Wellness Counseling</div>
    <p class="return-address">2875 Pellham Ridge Blvd., Suite 204<br>Larkfield, KS 63412</p>
  </section>

  <section class="sheet envelope-back" aria-label="Envelope back">
    <svg width="408" height="202" viewBox="0 0 408 202">
      <path d="M4 4 L196 96 Q204 100 212 96 L404 4" fill="none" stroke="var(--flap-line)" stroke-width="0.8" stroke-dasharray="2 1.5"/>
    </svg>
    <div class="wordmark"><span class="wordmark-dot"></span>Harborview Wellness Counseling</div>
  </section>

  <section class="sheet letterhead" aria-label="Letterhead">
    <div class="wordmark"><span class="wordmark-dot"></span>Harborview Wellness Counseling</div>
    <div class="letterhead-emblem" role="img" aria-label="Faint brand emblem area"></div>
    <p class="letterhead-footer">2875 Pellham Ridge Blvd., Suite 204, Larkfield, KS 63412 &nbsp;|&nbsp; Phone: 555-201-0142 &nbsp;|&nbsp; Fax: 555-201-0178</p>
  </section>

  <section class="sheet business-card" aria-label="Business card">
    <div class="card-name"><strong>Martin Oakridge</strong><span>Owner/Manager</span></div>
    <p class="card-contact">2875 Pellham Ridge Blvd., Suite 204, Larkfield, KS 63412<br>Phone 555.201.0142 | Fax 555.201.0178<br>oakridgehome@brisknet-mail.net</p>
    <div class="wordmark"><span class="wordmark-dot"></span>Harborview Wellness</div>
  </section>
</main>
</body>
</html>
```